Tavenorix - world unique technology for better life - please let them know who am i at first sight

We need a new business card for company which is a provider of unique crystal based technology suitable for all living being. For more information and final design you can use our brochure (our colours are black and blue from brochure).
We use Verdana font

Industry/Entity Type

Business

Contact Information for Business Card

regular dimension

Font styles to use
Other font styles liked:
• Verdana

Requirements
Must have
• Logo
• name
• function/position
• phone
• mobile
• e-mail
• adress
Nice to have
• inovative design (technology directed)

```html
<!DOCTYPE html>
<html lang="en">
<head>
<meta charset="utf-8">
<title>Tavenorix Technologies – Business Card</title>
<link rel="stylesheet" href="https://fonts.googleapis.com/css2?family=Open+Sans:ital,wght@0,300;0,400;0,700;0,800;1,400&display=swap">
<style>
  :root {
    --page-bg: #e4e5e6;
    --brand-blue: #1fa6de;
    --brand-blue-deep: #0f92cc;
    --brand-blue-text: #1b8fd0;
    --card-white: #f4f5f5;
    --ink-white: #ffffff;
    --card-shadow: rgba(0, 0, 0, 0.18);
  }
  * { box-sizing: border-box; margin: 0; padding: 0; }
  html, body {
    width: 1200px;
    height: 1000px;
    overflow: hidden;
    background: var(--page-bg);
    font-family: "Open Sans", Verdana, sans-serif;
  }
  .canvas {
    position: relative;
    width: 1200px;
    height: 1000px;
  }
  .card {
    position: absolute;
    left: 250px;
    width: 700px;
    height: 400px;
    overflow: hidden;
    box-shadow: 0 6px 18px var(--card-shadow);
  }

  /* Front side */
  .card--front {
    top: 70px;
    background: linear-gradient(160deg, var(--brand-blue) 0%, var(--brand-blue-deep) 100%);
    display: flex;
    align-items: center;
    justify-content: center;
  }
  .wordmark {
    display: flex;
    align-items: center;
    gap: 22px;
    color: var(--ink-white);
    font-weight: 300;
  }
  .wordmark__dot {
    width: 92px;
    height: 92px;
    border-radius: 50%;
    background: var(--ink-white);
    flex: none;
  }
  .wordmark__name {
    font-size: 50px;
    letter-spacing: 3px;
    line-height: 1;
  }
  .wordmark__sub {
    display: block;
    font-size: 17px;
    letter-spacing: 12px;
    margin-top: 8px;
  }

  /* Back side */
  .card--back {
    top: 530px;
    background: var(--brand-blue);
  }
  .card__info-panel {
    position: absolute;
    left: 0;
    top: 0;
    width: 390px;
    height: 305px;
    background: var(--card-white);
    border-top-left-radius: 72% 62%;
  }
  .card__footer-white {
    position: absolute;
    left: 0;
    top: 352px;
    width: 305px;
    height: 48px;
    background: var(--card-white);
  }
  .card__address-band {
    position: absolute;
    left: 0;
    top: 305px;
    width: 390px;
    height: 47px;
    display: flex;
    align-items: center;
    padding-left: 40px;
    color: var(--ink-white);
    font-size: 15px;
    letter-spacing: 0.3px;
  }
  .person {
    position: absolute;
    left: 200px;
    top: 42px;
    text-align: center;
    color: var(--brand-blue-text);
  }
  .person__name {
    font-size: 22px;
    font-weight: 800;
  }
  .person__role {
    font-size: 15px;
    font-style: italic;
    margin-top: -2px;
  }
  .contact {
    position: absolute;
    left: 40px;
    top: 190px;
    list-style: none;
    color: var(--brand-blue-text);
    font-size: 17px;
    line-height: 25px;
    letter-spacing: 0.5px;
  }
  .card--back .wordmark {
    position: absolute;
    left: 412px;
    top: 42px;
    gap: 12px;
  }
  .card--back .wordmark__dot { width: 52px; height: 52px; }
  .card--back .wordmark__name { font-size: 27px; letter-spacing: 2px; }
  .card--back .wordmark__sub { font-size: 10px; letter-spacing: 6px; margin-top: 4px; }
  .card__decor {
    position: absolute;
    left: 430px;
    top: 140px;
    width: 245px;
    height: 245px;
    border-radius: 50%;
    background: radial-gradient(circle, rgba(255,255,255,0) 38%, rgba(255,255,255,0.18) 55%, rgba(255,255,255,0.06) 72%, rgba(255,255,255,0) 74%);
  }
</style>
</head>
<body>
<main class="canvas">

  <section class="card card--front" aria-label="Business card front">
    <div class="wordmark">
      <span class="wordmark__dot"></span>
      <div>
        <span class="wordmark__name">TAVENORIX</span>
        <span class="wordmark__sub">TECHNOLOGIES</span>
      </div>
    </div>
  </section>

  <section class="card card--back" aria-label="Business card back">
    <div class="card__info-panel"></div>
    <div class="card__footer-white"></div>
    <div class="card__address-band">Address which you want to provide</div>

    <div class="person">
      <p class="person__name">Your Name</p>
      <p class="person__role">Position</p>
    </div>

    <ul class="contact">
      <li>Phone : 012- 345- 6789</li>
      <li>Mobile : 098- 765- 4321</li>
      <li>Email : yourname@mail.com</li>
    </ul>

    <div class="wordmark">
      <span class="wordmark__dot"></span>
      <div>
        <span class="wordmark__name">TAVENORIX</span>
        <span class="wordmark__sub">TECHNOLOGIES</span>
      </div>
    </div>

    <div class="card__decor" role="img" aria-label="Faint crystal sphere pattern decoration"></div>
  </section>

</main>
</body>
</html>
```